Re design and optimization of a website for pension Ora Vahi, a b&b in Tahiti, French Polynesia.

We have a website already : www.pensionoravahi.example

The general idea is to create a new site that is colorful, young and with an exotic, tropical feel since we are on a beautiful island.

The website will be in three languages, all the text is already available on our website, nothing changes.

All pages must have the name of the website (pension ora vahi b&b) our address, mail and phone number
It would be nice to have a link to our mail from every page

Sections have to be easy to update : text and pics

The sections needed are :

- Home page (accueil)

- Prices (tarifs)

- Bookings (reservations) = link to our mailbox : pensionoravahi@post.example )

- Pictures : in three separate categories that will pop up on this page : 1/ pics of the b&b 2/ pics of the surroundings 3/ customer's pics (we'll give new pics, not the current ones)

- Map of Tahiti : we'd like one map that we'll give you and also a Google map with our location, date and local time would be great

- Links (liens)

We let you see what would look best for the top banner and the switches, matching the logo and the pictures, make it nice and tropical !!
We have a few layouts that we did, maybe you will have a better idea of what we want by looking at them, if you can use them and have a good overall feel

We'd like to remind you guys that Tahiti is a dream destination, so you have to come up with something that the visitors will go : wow !!

We cater for backpackers to mid range accommodations and families, it all about a relaxed friendly atmosphere here !

NOTE THAT WE DON'T KNOW MUCH ABOUT PROGRAMMING AND CODING SO IT AS TO BE READY TO GO ON-LINE, ALL YOUR HELP IS APPRECIATED !!!
Also in Tahiti, the
INTERNET is quite low bandwidth so optimization is a must !

P.S : Live demo of the homepage is welcome ;)

We are available to all you for extra infos, good luck

regards,

remy & Pension Ora Vahi

Target Market(s)

Families and couples : individual rooms

Backpackers : Dormitories

people looking for an authentic stay in a familial environment

Customers of all ages and all nationalities

Requirements
Must have
• You must insist on the main page about :
the easy beach access
the breakfast included (with French baguette !)
Airport pick up 24/7
Many activities departing from our place : scuba diving, canyoning, 4x4 tour, rental cars, surf school, para-glide....

Please find a great way to highlight these !

```html
<!DOCTYPE html>
<html lang="en">
<head>
<meta charset="utf-8">
<title>Pension Ora Vahi – Tahiti</title>
<link rel="stylesheet" href="https://fonts.googleapis.com/css2?family=Baloo+2:wght@700&family=Lora:ital,wght@0,400;0,600;1,400;1,600&display=swap">
<style>
  :root {
    --pink: #c3139b;
    --pink-bright: #d61ab0;
    --teal: #14858f;
    --sky-top: #1f7fd6;
    --sky-mid: #4aa3e6;
    --lagoon: #45c6cf;
    --lagoon-deep: #1b9fb8;
    --panel: rgba(240, 250, 253, 0.94);
    --frame: rgba(220, 240, 250, 0.45);
    --white: #ffffff;
  }
  * { box-sizing: border-box; margin: 0; padding: 0; }
  html, body { width: 1200px; height: 1046px; overflow: hidden; }
  body {
    position: relative;
    font-family: "Lora", Georgia, serif;
    color: var(--teal);
    background: var(--sky-top);
  }
  .scenery {
    position: absolute; inset: 0;
    background:
      radial-gradient(ellipse 420px 160px at 1000px 800px, rgba(150, 130, 100, 0.45), transparent 70%),
      linear-gradient(180deg, var(--sky-top) 0%, var(--sky-mid) 30%, #6cc3d8 40%, var(--lagoon) 55%, var(--lagoon-deep) 80%, #2cb3c6 100%);
  }
  .flower {
    position: absolute; left: 40px; top: 25px; width: 315px; height: 290px;
    border-radius: 50%;
    background: radial-gradient(circle at 50% 48%, rgba(236, 96, 180, 0.85) 0%, rgba(236, 96, 180, 0.55) 45%, rgba(236, 96, 180, 0) 72%);
  }
  .brand {
    position: absolute; left: 474px; top: 34px;
    font-family: "Baloo 2", sans-serif; font-weight: 700;
    font-size: 38px; line-height: 50px; color: var(--white); letter-spacing: 1px;
  }
  .phone-box {
    position: absolute; left: 832px; top: 83px; width: 150px; height: 52px;
    background: rgba(225, 240, 250, 0.85); border-radius: 8px 8px 0 0;
    text-align: center; color: var(--pink);
  }
  .phone-box .label { font-size: 10px; font-weight: 600; letter-spacing: 1.5px; margin-top: 9px; }
  .phone-box .number { font-size: 17px; font-weight: 600; letter-spacing: 1.5px; line-height: 18px; }
  .main-nav {
    position: absolute; left: 318px; top: 133px; width: 882px; height: 44px;
    background: linear-gradient(90deg, var(--pink) 0%, var(--pink-bright) 70%, rgba(214, 26, 176, 0) 100%);
  }
  .main-nav a {
    position: absolute; top: 8px;
    font-family: "Baloo 2", sans-serif; font-weight: 700; font-size: 18px;
    color: var(--white); text-decoration: none; letter-spacing: 0.6px;
  }
  .nav-marker {
    position: absolute; left: 365px; top: 177px; width: 0; height: 0;
    border-left: 8px solid transparent; border-right: 8px solid transparent;
    border-top: 8px solid var(--pink); z-index: 3;
  }
  .frame {
    position: absolute; left: 213px; top: 177px; width: 769px; height: 605px;
    background: var(--frame); border-radius: 0 0 32px 32px;
  }
  .content {
    position: absolute; left: 257px; top: 177px; width: 683px; height: 468px;
    background: var(--panel); border-radius: 0 8px 0 0;
    padding: 34px 0 0 48px;
  }
  .lang {
    position: absolute; right: 25px; top: 17px;
    font-size: 10px; letter-spacing: 1.5px; color: var(--teal);
  }
  .lang b { color: var(--pink); font-weight: 600; }
  h1 {
    font-style: italic; font-weight: 400; color: var(--pink);
    font-size: 40px; letter-spacing: 5px; line-height: 42px;
  }
  h1 span { display: block; font-size: 25px; letter-spacing: 3.6px; line-height: 32px; }
  .rule { width: 560px; height: 1px; background: linear-gradient(90deg, #d7a5e0, rgba(215,165,224,0.2)); margin: 18px 0 24px -4px; }
  .content p, .content li { font-size: 11px; letter-spacing: 0.7px; line-height: 15.5px; }
  .content p { margin-bottom: 14px; }
  .hl { color: var(--pink); font-weight: 600; font-size: 12px; letter-spacing: 0.9px; }
  .content ul { list-style: none; margin: 0 0 14px 15px; }
  .content li::before { content: "> "; }
  .content p.extras { margin: -6px 0 0; }
  .gallery { position: absolute; left: 257px; top: 645px; display: flex; height: 95px; }
  .gallery div { height: 95px; }
  .arrow { position: absolute; top: 681px; width: 14px; height: 20px; }
  .bubble { position: absolute; left: 996px; top: 310px; width: 162px; height: 118px; }
  .bubble-text {
    position: absolute; left: 1012px; top: 335px; width: 126px; text-align: center;
    font-style: italic; font-size: 17px; letter-spacing: 1.5px; line-height: 21px; color: var(--pink);
  }
  .newsletter { position: absolute; left: 276px; top: 802px; }
  .newsletter label { display: block; color: var(--white); font-size: 11px; font-weight: 600; letter-spacing: 1.2px; }
  .newsletter .field {
    margin: 10px 0 0 23px; width: 185px; height: 26px; border-radius: 6px;
    background: rgba(230, 245, 250, 0.6);
  }
  .footer-wave { position: absolute; left: 0; top: 880px; }
  .site-footer {
    position: absolute; left: 0; top: 934px; width: 1200px; text-align: center;
    color: var(--white); font-size: 11px; font-weight: 600; letter-spacing: 1.3px; line-height: 17px;
  }
</style>
</head>
<body>
  <div class="scenery" role="img" aria-label="Tropical sky over a turquoise lagoon with overwater bungalows and a small boat"></div>
  <div class="flower" role="img" aria-label="Pink water lily flower"></div>

  <header>
    <div class="brand">PENSION ORA VAHI</div>
    <div class="phone-box"><div class="label">TELEPHONE</div><div class="number">(00) 47 12 90</div></div>
    <nav class="main-nav">
      <a href="#" style="left:22px">ACCUEIL</a>
      <a href="#" style="left:119px">TARIFS</a>
      <a href="#" style="left:212px">RESERVATION</a>
      <a href="#" style="left:354px">PHOTOS</a>
      <a href="#" style="left:448px">NEWS</a>
      <a href="#" style="left:528px">TAHITI</a>
    </nav>
  </header>
  <div class="nav-marker"></div>

  <div class="frame"></div>
  <main class="content">
    <div class="lang"><b>FRA</b> / ENG / ESP</div>
    <h1>PARADISE<span>IN THE MIDDLE OF PACIFIC OCEAN</span></h1>
    <div class="rule"></div>
    <p><span class="hl">PENSION ORA VAHI</span> is located in the Paea district - 18,6 kms from Papeete - mountain side.<br>200 meters from the nicest white sand beach of TAHITI French Polynesia</p>
    <p><span class="hl">BED &amp; BREAKFAST</span><br>with a friendly atmosphere - breakfast included every morning at the terrace in the garden<br>self-service between 7h30 to 10h30 with a fantastic view at the mountain...</p>
    <p style="margin-bottom:0"><span class="hl">LA PENSION ORA VAHI EST COMPOSÉE DE 3 MAISONS D'HABITATION comprenant :</span></p>
    <ul>
      <li>1 Reception (tel - fax - internet)</li>
      <li>5 chambres individuelles ou familiales</li>
      <li>2 dortoirs (4 places chacun)</li>
      <li>plusieures cuisines équipées (gazinière, frigidaire, micro-ondes, vaisselle à disposition)</li>
      <li>sanitaires communs</li>
      <li>télévision et coin bibliothèque</li>
      <li>nombreuses terrasses - grands jardins (hamacs, relax)</li>
      <li>accès plage facile (à 200 mètres de la pension)</li>
    </ul>
    <p><span class="hl">Bagages :</span> consigne gratuite (pour un retour d'une nuit minimum à la pension)</p>
    <p class="extras"><span class="hl">Airport pick up 24/7 :</span> activités au départ de la pension - plongée, canyoning, 4x4, surf school</p>
  </main>

  <div class="gallery">
    <div style="width:141px;background:linear-gradient(160deg,#7fb7d8,#2f8fa8 60%,#1d6f7a)" role="img" aria-label="Surfer riding a wave"></div>
    <div style="width:137px;background:linear-gradient(170deg,#1e4f9c,#4fa9d6 55%,#d8eef2)" role="img" aria-label="Aerial view of a lagoon atoll"></div>
    <div style="width:136px;background:linear-gradient(160deg,#2b5f9a,#d4892e 55%,#a0522d)" role="img" aria-label="Polynesian painting"></div>
    <div style="width:134px;background:linear-gradient(160deg,#7aa36a,#3f7a36 55%,#26541f)" role="img" aria-label="Green mountain valley"></div>
    <div style="width:135px;background:linear-gradient(160deg,#3fc0c8,#1a99a8 60%,#137f8e)" role="img" aria-label="Sea turtle swimming"></div>
  </div>
  <svg class="arrow" style="left:229px" viewBox="0 0 14 20"><path d="M11 2 L3 10 L11 18" fill="none" stroke="#c3139b" stroke-width="3.5"/></svg>
  <svg class="arrow" style="left:954px" viewBox="0 0 14 20"><path d="M3 2 L11 10 L3 18" fill="none" stroke="#c3139b" stroke-width="3.5"/></svg>

  <svg class="bubble" viewBox="0 0 162 118" aria-hidden="true">
    <path d="M81 4 C125 4 158 22 158 48 C158 72 132 88 96 91 L70 114 L72 92 C34 88 4 72 4 48 C4 22 37 4 81 4 Z" fill="#7ed3e8" stroke="#b56bd6" stroke-width="4"/>
  </svg>
  <div class="bubble-text">"Ia orana<br>e maeva!</div>

  <form class="newsletter">
    <label>e-mail for newsletter and more info</label>
    <div class="field"></div>
  </form>

  <svg class="footer-wave" width="1200" height="166" viewBox="0 0 1200 166" aria-hidden="true">
    <defs><linearGradient id="footerFill" x1="0" y1="0" x2="0" y2="1"><stop offset="0" stop-color="#c3139b"/><stop offset="1" stop-color="#a80c8a"/></linearGradient></defs>
    <path d="M0 18 q25 -14 50 0 t50 0 t50 0 t50 0 t50 0 t50 0 t50 0 t50 0 t50 0 t50 0 t50 0 t50 0 t50 0 t50 0 t50 0 t50 0 t50 0 t50 0 t50 0 t50 0 t50 0 t50 0 t50 0 t50 0 V166 H0 Z" fill="url(#footerFill)" stroke="#e04cc4" stroke-width="3"/>
  </svg>
  <footer class="site-footer">
    TEL/FAX : (00 ) 47 12 90<br>
    BP 140022 PAEA 98711 VALLÉE HAUTE TAHITI - FRENCH POLYNESIA<br>
    E MAIL : PENSIONORAVAHI@POST.EXAMPLE<br>
    WEB SIDE : WWW.PENSIONORAVAHI.EXAMPLE
  </footer>
</body>
</html>
```